Business Card Design Project

After recently finishing a design project for the company logo using quillnest, it's now time for a business card. Attached to this is the logo.

The requirements for the business card are pretty straightforward:

- A clean, uncomplicated look
- Consistent usage of fonts
- Designs for both single sided and double sided cards
- A modern layout with preferably space to refer to social media accounts and/or downloadable vcards through a qr code
- consistent application of the company colour scheme: red/white. Hex codes for exact colour can be provided

Thanks!

```html
<!DOCTYPE html>
<html lang="en">
<head>
<meta charset="utf-8">
<title>Ashford Recruiting – Business Card</title>
<link rel="stylesheet" href="https://fonts.googleapis.com/css2?family=Open+Sans:ital,wght@0,400;0,600;0,700;1,700&display=swap">
<style>
  :root {
    --brand-red: #e21f2b;
    --ink: #231f20;
    --muted: #8a8a8a;
    --rule: #b9b9bd;
    --paper: #ffffff;
    --backdrop: #e9e7e4;
  }
  * { margin: 0; padding: 0; box-sizing: border-box; }
  html, body { width: 960px; height: 1200px; overflow: hidden; }
  body {
    position: relative;
    background: var(--backdrop);
    font-family: "Open Sans", Arial, sans-serif;
    color: var(--ink);
  }
  .card {
    position: absolute;
    left: 60px;
    width: 840px;
    height: 480px;
    background: var(--paper);
    border-radius: 32px;
    overflow: hidden;
  }
  .card--front { top: 77px; }
  .card--back { top: 637px; }

  .brand {
    position: absolute;
    left: 0; right: 0;
    display: flex;
    align-items: center;
    justify-content: center;
    gap: 26px;
  }
  .card--front .brand { top: 100px; }
  .card--back .brand { top: 170px; }
  .brand__mark {
    width: 62px; height: 62px;
    background: var(--brand-red);
  }
  .brand__name {
    font-size: 64px;
    font-weight: 600;
    letter-spacing: -1px;
    color: var(--ink);
    line-height: 1;
  }

  .rule {
    position: absolute;
    left: 0; right: 0;
    height: 3px;
    background: var(--rule);
  }
  .rule--top { top: 274px; }
  .rule--bottom { top: 391px; }

  .info-band {
    position: absolute;
    top: 281px;
    left: 0; right: 0;
    height: 107px;
    background: var(--brand-red);
    color: var(--paper);
  }
  .person {
    position: absolute;
    left: 90px;
    top: 24px;
  }
  .person__name { font-size: 25px; font-weight: 700; line-height: 1.2; }
  .person__role { font-size: 20px; font-weight: 400; line-height: 1.4; }
  .info-band__divider {
    position: absolute;
    left: 419px;
    top: 20px;
    width: 2px;
    height: 68px;
    background: #8f1018;
  }
  .address {
    position: absolute;
    right: 90px;
    top: 24px;
    text-align: right;
    font-size: 22px;
    line-height: 1.35;
  }
  .contact {
    position: absolute;
    top: 405px;
    left: 0; right: 0;
    text-align: center;
    font-size: 20px;
    line-height: 1.45;
  }
  .contact__label { font-weight: 700; font-style: italic; }
  .contact__sep { margin: 0 8px; }
</style>
</head>
<body>
  <section class="card card--front">
    <div class="brand">
      <span class="brand__mark"></span>
      <span class="brand__name">Ashford Recruiting</span>
    </div>

    <div class="rule rule--top"></div>
    <div class="info-band">
      <div class="person">
        <p class="person__name">Your Name</p>
        <p class="person__role">Designation</p>
      </div>
      <div class="info-band__divider"></div>
      <p class="address">1234, Street Name, District<br>City, Country Code.</p>
    </div>
    <div class="rule rule--bottom"></div>

    <div class="contact">
      <p><span class="contact__label">t</span> : 123-123-1234</p>
      <p><span class="contact__label">e</span> : info@yourwebsite.com<span class="contact__sep">|</span><span class="contact__label">w</span> : www.ashfordrec.com</p>
    </div>
  </section>

  <section class="card card--back">
    <div class="brand">
      <span class="brand__mark"></span>
      <span class="brand__name">Ashford Recruiting</span>
    </div>
  </section>
</body>
</html>
```